Logo for Brisk Partners LLC needs a design

This logo will be for a food handler and restaurant manager training business located. I am a registered trainer and proctor for KitchGuard, the Federal Dining League. colors options should be black, white, blue, silver or something else bold. The file that I have sent needs to be on the card somewhere, small.
Updates

need to have the KitchGuard logo that I added on the card. BRISK stands for basic regulated instruction for service kitchens.

Logo Text

Dennis JonesStar ,Associates LLC. , Registered trainer and proctorwith KitchGuard.

```html
<!DOCTYPE html>
<html lang="en">
<head>
<meta charset="utf-8">
<title>Brisk Partners LLC — Business Card</title>
<link rel="stylesheet" href="https://fonts.googleapis.com/css2?family=Montserrat:wght@400;500;600&family=Tinos:wght@700&display=swap">
<style>
  :root {
    --backdrop: #1a1a1a;
    --card: #232323;
    --accent: #1ea7e1;
    --brand-blue: #2a4fa8;
    --silver: #3c3c3c;
    --silver-light: #c4c4c4;
    --text: #f2f2f2;
    --muted: #d8d8d8;
  }
  * { margin: 0; padding: 0; box-sizing: border-box; }
  html, body { width: 1200px; height: 900px; overflow: hidden; background: var(--backdrop); }
  body { font-family: "Montserrat", Arial, sans-serif; color: var(--text); position: relative; }

  .card {
    position: absolute; left: 270px; width: 660px; height: 378px; overflow: hidden;
    background: var(--card);
    border-bottom: 6px solid var(--accent);
    box-shadow: 0 14px 30px rgba(0,0,0,.55);
  }
  .card--front { top: 40px; }
  .card--back { top: 470px; }

  .brand-row { display: flex; align-items: center; white-space: nowrap; }
  .brand-mark { flex: none; border-radius: 50%; }

  /* Front */
  .front-lockup { position: absolute; top: 112px; left: 0; right: 0; display: flex; flex-direction: column; align-items: center; }
  .front-lockup .brand-row { gap: 12px; }
  .front-lockup .brand-name {
    font-size: 46px; font-weight: 500; color: var(--silver); letter-spacing: 1px; line-height: 1.05;
  }
  .front-lockup .brand-mark { width: 52px; height: 52px; background: var(--silver-light); }
  .front-lockup .brand-sub {
    font-size: 26px; font-weight: 500; color: var(--silver); letter-spacing: 1px; margin-top: 0;
  }
  .front-lockup .tagline { font-size: 19px; color: #9a9a9a; margin-top: 6px; letter-spacing: .5px; white-space: nowrap; }

  /* Back */
  .back-lockup { position: absolute; left: 28px; top: 92px; width: 330px; }
  .back-lockup .brand-row { gap: 8px; }
  .back-lockup .brand-name { font-size: 29px; font-weight: 500; color: var(--brand-blue); line-height: 1.05; }
  .back-lockup .brand-mark { width: 32px; height: 32px; background: var(--accent); }
  .back-lockup .brand-sub { font-size: 18px; font-weight: 500; color: var(--accent); margin-left: 86px; margin-top: 2px; }
  .back-lockup .tagline { font-size: 13px; color: var(--text); margin-top: 4px; white-space: nowrap; }

  .partner-badge { position: absolute; left: 56px; top: 218px; }
  .partner-caption {
    position: absolute; left: 44px; top: 282px;
    font-family: "Tinos", "Times New Roman", serif; font-weight: 700; font-size: 13px; line-height: 1.2; color: var(--text);
  }

  .divider { position: absolute; left: 372px; top: 58px; width: 2px; height: 240px; background: var(--accent); }

  .contact { position: absolute; left: 394px; top: 62px; width: 250px; }
  .contact .person { font-size: 28px; font-weight: 500; color: var(--accent); letter-spacing: 1.5px; line-height: 1; white-space: nowrap; }
  .contact .role { font-size: 17px; color: var(--muted); margin-top: 4px; }
  .contact .address { font-size: 17px; color: var(--text); margin-top: 14px; line-height: 1.3; }
  .contact ul { list-style: none; margin-top: 10px; }
  .contact li { display: flex; align-items: center; gap: 9px; font-size: 16px; line-height: 1.55; white-space: nowrap; }
  .contact li svg { width: 13px; height: 13px; flex: none; }
</style>
</head>
<body>

<section class="card card--front">
  <div class="front-lockup">
    <div class="brand-row">
      <span class="brand-name">Marvin PeltBrisk</span>
      <span class="brand-mark"></span>
    </div>
    <div class="brand-sub">Partners LLC.</div>
    <div class="tagline">Registered trainer and proctor with KitchGuard.</div>
  </div>
</section>

<section class="card card--back">
  <div class="back-lockup">
    <div class="brand-row">
      <span class="brand-name">Marvin PeltBrisk</span>
      <span class="brand-mark"></span>
    </div>
    <div class="brand-sub">Partners LLC.</div>
    <div class="tagline">Registered trainer and proctor with KitchGuard.</div>
  </div>

  <svg class="partner-badge" width="150" height="56" viewBox="0 0 150 56" role="img" aria-label="KitchGuard partner badge">
    <rect x="0" y="6" width="150" height="44" rx="6" fill="var(--accent)" opacity=".85"/>
  </svg>
  <div class="partner-caption">Registered KitchGuard Proctor<br>&amp; Certified KitchGuard Instructor</div>

  <div class="divider"></div>

  <div class="contact">
    <div class="person">DORIAN VALE</div>
    <div class="role">Director</div>
    <div class="address">1185 Alder Lane<br>Northfield, MA 02190</div>
    <ul>
      <li>
        <svg viewBox="0 0 14 14"><path d="M3 1l2 3-1.2 1.3a8 8 0 0 0 4.9 4.9L10 9l3 2-1.3 2.2C6 13 1 8 .8 2.3z" fill="var(--accent)"/></svg>
        03 5518 2940
      </li>
      <li>
        <svg viewBox="0 0 14 14"><rect x="3.5" y="1" width="7" height="12" rx="1.2" fill="none" stroke="var(--accent)" stroke-width="1.4"/><circle cx="7" cy="11" r=".8" fill="var(--accent)"/></svg>
        0412 774 390
      </li>
      <li>
        <svg viewBox="0 0 14 14"><rect x="1" y="3" width="12" height="8" fill="none" stroke="var(--accent)" stroke-width="1.3"/><path d="M1 3l6 4.5L13 3" fill="none" stroke="var(--accent)" stroke-width="1.3"/></svg>
        info@marvinpeltbrisk.com
      </li>
      <li>
        <svg viewBox="0 0 14 14"><circle cx="7" cy="7" r="6" fill="none" stroke="var(--accent)" stroke-width="1.2"/><ellipse cx="7" cy="7" rx="2.6" ry="6" fill="none" stroke="var(--accent)" stroke-width="1"/><path d="M1 7h12M2 4h10M2 10h10" stroke="var(--accent)" stroke-width="1"/></svg>
        www.marvinpeltbrisk.com
      </li>
    </ul>
  </div>
</section>

</body>
</html>
```